I've recently started my own party promotion business. We are currently based in Sydney, Australia. Thus, most of our events are based in the Sydney Metropolitan area, with an eye to continue expanding our business and promote parties right through the Asia Pacific region.

Company details are as follows;

*Company name - Tovunde Promotions
*Company motto - The Midnight Revel Hosts
*Website - www.tovunde-example.com
*Phone number - 0462 307 194
*Employee Name - Bram Okonedi
*Employee Title - Executive Chief of Operations - Asia Pacific

We need the following items/templates designed;

1. Business Cards
2. Letterhead
3. Envelopes
4. Envelope seals/stickers

At the moment, I am using my mobile number as the main point of contact, for any enquiries. Thus I don't have a landline or fax number. I don't have my 'www.tovunde-example.com' website up and running yet either. Therefore, I would like the templates/designs provided to allow me to add those details at a later date, with ease.

1. Business card.
Note: Please be aware that the design provided will also act as a template to use for any future employees I take on board. Therefore I need to be able to edit the name, title and mobile number with ease.
A. Front Side. I would like my logo to be on the left with the company name to the right of the logo, along the top of the business card. With our company motto directly underneath. Then my name, title, mobile phone number and website following beneath.
B. On the reverse side of the card, I would like the full logo to be centred, with the motto underneath. I want both sides to be royal purple, with everything in glittering gold, consistent with my logo.

2. Letterhead.
A. I would like the full logo to be based to the top right hand corner. With the company motto following underneath.
B. Followed by three lines/spaces to add an address, phone number and fax number, when it becomes applicable. I want these details to be in gold without the purple background. Remembering I need to be able to edit these details when they become available.
C. I would like the website to be emblazoned in gold along the bottom, with the logo on each side of the website address. I also want these details to be in gold without the purple background.

3. Envelopes
Please use your creative expression for this particular template, so as long as it has a consistent matching feel with the Letterhead.

4. Envelope Seals/Stickers
Again, feel free to use your creative flair, so long as it's consistent with the other items. However, I would like these to be round. With only the logo included on the purple background.

If there are any questions, please call me on my mobile number. 0462 307 194.

Many thanks.

Bram

```html
<!DOCTYPE html>
<html lang="en">
<head>
<meta charset="utf-8">
<title>Tovunde Promotions – Business Card</title>
<link rel="stylesheet" href="https://fonts.googleapis.com/css2?family=Playfair+Display:ital,wght@0,400;1,400&display=swap">
<style>
  :root {
    --backdrop: #ebebed;
    --royal-purple: #46285a;
    --gold: #d6a62b;
    --card-shadow: 0 2px 4px rgba(0,0,0,0.18), 0 8px 18px rgba(0,0,0,0.08);
  }
  * { margin: 0; padding: 0; box-sizing: border-box; }
  html, body {
    width: 1200px; height: 800px; overflow: hidden;
    background: var(--backdrop);
    font-family: "Playfair Display", Georgia, serif;
    color: var(--gold);
  }
  .canvas { position: relative; width: 1200px; height: 800px; }

  .card {
    position: absolute;
    width: 476px; height: 306px;
    background: var(--royal-purple);
    box-shadow: var(--card-shadow);
    overflow: hidden;
  }
  .card--back  { left: 377px; top: 74px; }
  .card--front { left: 376px; top: 418px; }

  /* brand lockup */
  .brand { position: absolute; text-align: center; }
  .brand__mark {
    display: block; margin: 0 auto;
    border: 3px solid var(--gold); border-radius: 50%;
  }
  .brand__name {
    display: block;
    font-weight: 400; text-transform: uppercase;
    white-space: nowrap;
  }

  .card--back .brand { left: 0; right: 0; top: 52px; }
  .card--back .brand__mark { width: 130px; height: 130px; }
  .card--back .brand__name { margin-top: 34px; font-size: 26px; letter-spacing: 0.12em; }

  .card--front .brand { left: 303px; width: 180px; top: 22px; }
  .card--front .brand__mark { width: 82px; height: 82px; border-width: 2px; }
  .card--front .brand__name { margin-top: 16px; font-size: 12px; letter-spacing: 0.08em; }
  .brand__motto {
    display: block; margin-top: 6px;
    font-style: italic; font-size: 10.5px; white-space: nowrap;
  }

  /* contact details */
  .contact { position: absolute; left: 22px; top: 188px; font-style: italic; }
  .contact__name  { font-size: 18px; line-height: 1.2; }
  .contact__title { font-size: 13.5px; margin-top: 3px; }
  .contact__list  { margin-top: 12px; font-size: 13px; }
  .contact__row   { display: flex; line-height: 24px; }
  .contact__label { width: 44px; font-size: 12px; }
</style>
</head>
<body>
<main class="canvas">

  <section class="card card--back" aria-label="Business card, reverse side">
    <div class="brand">
      <span class="brand__mark" aria-hidden="true"></span>
      <span class="brand__name">Tovunde Promotions</span>
    </div>
  </section>

  <section class="card card--front" aria-label="Business card, front side">
    <div class="brand">
      <span class="brand__mark" aria-hidden="true"></span>
      <span class="brand__name">Tovunde Promotions</span>
      <span class="brand__motto">The Midnight Revel Hosts</span>
    </div>

    <div class="contact">
      <p class="contact__name">Bram Okonedi</p>
      <p class="contact__title">Executive Chief of Operations - Asia Pacific</p>
      <div class="contact__list">
        <p class="contact__row"><span class="contact__label">tel</span><span>0462 307 194</span></p>
        <p class="contact__row"><span class="contact__label">web</span><span>www.tovunde-example.com</span></p>
      </div>
    </div>
  </section>

</main>
</body>
</html>
```